Carpet cleaning company wants business card

Need an exciting new fresh design for business cards for my carpet cleaning /pest control business
www.tidewellhomecare.com.au
Can design include a lined section for quoting or information? Thanks !

```html
<!DOCTYPE html>
<html lang="en">
<head>
<meta charset="utf-8">
<title>Tidewell Home Care – Business Card</title>
<link rel="stylesheet" href="https://fonts.googleapis.com/css2?family=Arimo:wght@400;700&display=swap">
<style>
  :root {
    --brand-blue: #0d57a6;
    --accent-red: #e8383d;
    --card-white: #ffffff;
    --backdrop: #e4e4e4;
    --logo-cyan: #36d6f2;
    --text-light: #ffffff;
    --rule-grey: #b9c7d8;
  }
  html, body {
    margin: 0;
    padding: 0;
    width: 1200px;
    height: 1040px;
    overflow: hidden;
    background: var(--backdrop);
    font-family: "Arimo", Arial, sans-serif;
  }
  .canvas {
    position: relative;
    width: 1200px;
    height: 1040px;
  }
  .card {
    position: absolute;
    left: 285px;
    width: 640px;
    height: 366px;
    border-radius: 20px;
    overflow: hidden;
    box-shadow: 0 2px 4px rgba(0,0,0,0.35);
  }
  .card--front { top: 130px; background: var(--card-white); }
  .card--back  { top: 568px; background: var(--brand-blue); }

  .front-shape { position: absolute; inset: 0; }

  .holder {
    position: absolute;
    left: 24px;
    top: 84px;
    color: var(--text-light);
  }
  .holder__name {
    margin: 0;
    font-size: 25px;
    font-weight: 700;
    line-height: 1.1;
  }
  .holder__title {
    margin: 2px 0 0;
    font-size: 14px;
    font-weight: 400;
  }

  .contact-list {
    position: absolute;
    left: 24px;
    top: 200px;
    margin: 0;
    padding: 0;
    list-style: none;
    color: var(--text-light);
    font-size: 15px;
    line-height: 19px;
  }
  .contact-list li {
    display: flex;
    align-items: center;
    gap: 6px;
  }
  .contact-list svg { width: 13px; height: 13px; flex: none; }

  .wordmark {
    position: absolute;
    margin: 0;
    left: 345px;
    top: 166px;
    width: 272px;
    text-align: center;
    color: var(--brand-blue);
    font-size: 28px;
    font-weight: 700;
    line-height: 32px;
    letter-spacing: -0.5px;
    white-space: nowrap;
  }

  .quote-lines {
    position: absolute;
    left: 395px;
    top: 226px;
    width: 218px;
    height: 90px;
  }

  .wordmark--back {
    left: 0;
    top: 158px;
    width: 640px;
    color: var(--logo-cyan);
    font-size: 44px;
    line-height: 50px;
  }
</style>
</head>
<body>
<main class="canvas">

  <section class="card card--front" aria-label="Business card front">
    <svg class="front-shape" viewBox="0 0 640 366" preserveAspectRatio="none" aria-hidden="true">
      <polygon points="0,0 442,0 266,182 442,366 0,366" fill="var(--brand-blue)"/>
      <polyline points="451,-4 281,182 451,370" fill="none" stroke="var(--accent-red)" stroke-width="5"/>
    </svg>

    <div class="holder">
      <h1 class="holder__name">Liam Porter</h1>
      <p class="holder__title">President</p>
    </div>

    <ul class="contact-list">
      <li>
        <svg viewBox="0 0 16 16"><path fill="currentColor" d="M3.5 1l2.5 3-1.5 1.8c.9 2 2.6 3.7 4.6 4.6L11 8.9l3 2.6-1.4 2.8C7 14 2 9 1.7 3.4z"/></svg>
        07 5182 6640
      </li>
      <li>
        <svg viewBox="0 0 16 16"><rect x="4" y="1" width="8" height="14" rx="1.5" fill="none" stroke="currentColor" stroke-width="1.6"/><rect x="5.5" y="3" width="5" height="8" fill="currentColor"/></svg>
        0427 593 214
      </li>
      <li>
        <svg viewBox="0 0 16 16"><rect x="1" y="4" width="14" height="9" fill="currentColor"/><path d="M1.5 4.5L8 9.5l6.5-5" fill="none" stroke="var(--brand-blue)" stroke-width="1.3"/></svg>
        admin@tidewellhomecare.com.au
      </li>
      <li>
        <svg viewBox="0 0 16 16"><circle cx="8" cy="8" r="6.5" fill="currentColor"/><path d="M5 4c1 1 2 1 2 3s-2 1-2 3M10 12c0-2 2-2 2-4" fill="none" stroke="var(--brand-blue)" stroke-width="1.3"/></svg>
        www.tidewellhomecare.com.au
      </li>
    </ul>

    <p class="wordmark">Tidewell Home Care</p>

    <svg class="quote-lines" viewBox="0 0 218 90" aria-label="Lined area for quotes and notes">
      <line x1="0" y1="20" x2="218" y2="20" stroke="var(--rule-grey)" stroke-width="1"/>
      <line x1="0" y1="48" x2="218" y2="48" stroke="var(--rule-grey)" stroke-width="1"/>
      <line x1="0" y1="76" x2="218" y2="76" stroke="var(--rule-grey)" stroke-width="1"/>
    </svg>
  </section>

  <section class="card card--back" aria-label="Business card back">
    <p class="wordmark wordmark--back">Tidewell Home Care</p>
  </section>

</main>
</body>
</html>
```